Honey Bottle Labels for Honey Business

The honey is a niche product and the logo should exude a strong impression of wild and raw honey and natural – as in natural beekeeping. We try to keep things as simple as possible; this includes the processes the honey goes through.
We are looking for something with a gourmet / classy upmarket look and feel design. For example: Ideas with bees, honeycomb, modern or hexagonal feature; something eye catching, but not too busy.
Our honey is all natural and organic. We are a clean, simple yet sophisticated business, so would like our logo to reflect these principles.

Feel free to expand your creativity to anything you may think would look awesome and original!

The label needs to contain:
1. Our company logo. (Please see attached)
2. 100% Pure Raw Honey / Local
3. Net Wt: 16 oz (454 g) (this is the weight of the honey and will need to be modified based on bottle size.)
4. Address, Cedar Hollow, MN 56100 (not larger than 1/16th inch)

Needs to be versatile to include possibility of clear label, I have included some example pictures as ideas (oval, round, square tags)

Sizes needed:
Large oval 2 5/8" x 4 1/2"
Small oval: 1 3/4" wide x 3" tall
Rectangle 1 3/4" tall x 5" wide
Round diameter 2.5"

Target Market(s)

Gourmet stores, market stall, local tourist market, potential store door sales

Requirements
Must have
• - A design that can be used on various packaging, jars and containers. We are hoping to scale up the production and want something to suit.
• - has to have a wow to stand out on the supermarket shelves
Nice to have
• Things we like:
• Minimalist designs
• Clever designs
• We don't like hand drawn font types
• We are open to the use of a hexagon in the logo, but not must have
Should not have
• Things we do not like:
• Too many colors

```html
<!DOCTYPE html>
<html lang="en">
<head>
<meta charset="utf-8">
<title>Goldmeadow Honey – Jar Label</title>
<link rel="stylesheet" href="https://fonts.googleapis.com/css2?family=Comfortaa:wght@400;500&family=Arimo:wght@700&display=swap">
<style>
  :root {
    --paper: #ffffff;
    --honey-deep: #f5820f;
    --honey-mid: #f99a26;
    --honey-light: #fdb713;
    --ring: #f8aa1f;
    --label-text: #f59c1a;
    --ink: #222222;
  }
  * { margin: 0; padding: 0; box-sizing: border-box; }
  html, body { width: 1200px; height: 422px; overflow: hidden; background: var(--paper); }
  .label {
    position: relative;
    width: 1200px;
    height: 422px;
    background: var(--paper);
    overflow: hidden;
  }
  .comb {
    position: absolute;
    border-radius: 46%;
    background: radial-gradient(circle at 40% 40%, var(--honey-light) 0%, var(--honey-mid) 55%, var(--honey-deep) 100%);
  }
  .comb--top-left { left: 110px; top: -40px; width: 250px; height: 280px; }
  .comb--top-cap { left: 358px; top: -20px; width: 64px; height: 58px; }
  .comb--left-dot { left: 42px; top: 110px; width: 54px; height: 54px; background: var(--honey-deep); }
  .comb--mid-dot { left: 350px; top: 182px; width: 54px; height: 54px; background: var(--honey-light); }
  .comb--bottom-right { left: 862px; top: 148px; width: 244px; height: 300px; }
  .comb--right-dot { left: 1128px; top: 236px; width: 50px; height: 54px; background: var(--honey-deep); }
  .comb--upper-dot { left: 812px; top: 148px; width: 56px; height: 54px; background: var(--honey-light); }
  .comb--lower-dot { left: 796px; top: 344px; width: 54px; height: 56px; background: var(--honey-mid); }

  .seal {
    position: absolute;
    left: 395px;
    top: 13px;
    width: 400px;
    height: 400px;
  }
  .seal__ring { fill: none; stroke: var(--ring); stroke-width: 4; }
  .seal__claim, .seal__address {
    font-family: "Comfortaa", sans-serif;
    font-weight: 500;
    fill: var(--label-text);
  }
  .seal__claim { font-size: 23px; letter-spacing: 0.5px; }
  .seal__address { font-size: 16px; letter-spacing: 0.4px; }
  .seal__brand {
    font-family: "Comfortaa", sans-serif;
    font-weight: 500;
    fill: var(--honey-mid);
    font-size: 36px;
    text-anchor: middle;
  }

  .net-weight {
    position: absolute;
    left: 318px;
    top: 370px;
    width: 110px;
    font-family: "Arimo", sans-serif;
    font-weight: 700;
    font-size: 13px;
    line-height: 15px;
    color: var(--ink);
    text-align: center;
  }
</style>
</head>
<body>
<main class="label">
  <div class="comb comb--top-left" role="img" aria-label="Cluster of orange and amber honeycomb cells"></div>
  <div class="comb comb--top-cap" role="img" aria-label="Single honeycomb cell"></div>
  <div class="comb comb--left-dot" role="img" aria-label="Single honeycomb cell"></div>
  <div class="comb comb--mid-dot" role="img" aria-label="Single honeycomb cell"></div>
  <div class="comb comb--bottom-right" role="img" aria-label="Cluster of orange and amber honeycomb cells"></div>
  <div class="comb comb--right-dot" role="img" aria-label="Single honeycomb cell"></div>
  <div class="comb comb--upper-dot" role="img" aria-label="Single honeycomb cell"></div>
  <div class="comb comb--lower-dot" role="img" aria-label="Single honeycomb cell"></div>

  <svg class="seal" viewBox="0 0 400 400" aria-labelledby="seal-title">
    <title id="seal-title">Goldmeadow Honey – 100% Pure Raw Honey, Local</title>
    <defs>
      <path id="claim-arc" d="M 40,200 A 160,160 0 0 1 360,200"/>
      <path id="address-arc" d="M 40,200 A 160,160 0 0 0 360,200"/>
    </defs>
    <circle class="seal__ring" cx="200" cy="200" r="127"/>
    <text class="seal__claim">
      <textPath href="#claim-arc" startOffset="50%" text-anchor="middle">100% Pure Raw Honey / Local</textPath>
    </text>
    <text class="seal__brand" x="200" y="198">goldmeadow</text>
    <text class="seal__brand" x="200" y="240">honey</text>
    <text class="seal__address" dy="14">
      <textPath href="#address-arc" startOffset="50%" text-anchor="middle">Cedar Hollow, MN 56100</textPath>
    </text>
  </svg>

  <p class="net-weight">Net Wt: 10 oz<br>(283 g)</p>
</main>
</body>
</html>
```